Computer Security FaceBook start-up design.

Should be in Harmony with https://www.quillmora.com We need a design for our facebook profile for our company QuillMora. We work at computer security consulting services and licensing offering a high technological OtterPane. A Framework That Allows any security based company to analyze / monitorize / etc. really any application with high performance and stealth based on hypervisor technologies. Our main color is RED, as you will see in our logo. The design Should our deep expertise transmit / skills on security. We would like to have OtterPane Also Represented as Lynx With an Anything That Could That remark is Iberian Lynx (if possible). Any questions are welcome :)

Industry/Entity Type

Computer Security

Requirements
Must have
• Should be in armony With https://www.quillmora.com

```html
<!DOCTYPE html>
<html lang="en">
<head>
<meta charset="utf-8">
<title>QuillMora – Cover</title>
<link rel="stylesheet" href="https://fonts.googleapis.com/css2?family=Raleway:wght@400;500;600;700&display=swap">
<style>
  :root {
    --red: #e8434d;
    --red-dark: #d8343f;
    --navy: #3a4859;
    --navy-dark: #2f3b4a;
    --mist: #e3e8ee;
    --mist-light: #eef1f5;
    --ink: #3b3f46;
    --grey-text: #6c737c;
    --guide: #b9c0c8;
    --white: #ffffff;
  }
  * { margin: 0; padding: 0; box-sizing: border-box; }
  html, body { width: 1200px; height: 456px; overflow: hidden; background: var(--white); }
  body { font-family: "Raleway", Arial, sans-serif; color: var(--ink); }

  .cover { position: relative; width: 1200px; height: 456px; overflow: hidden; background: var(--white); }

  .backdrop { position: absolute; inset: 0; }

  .hero-visual {
    position: absolute; left: 0; top: 0; width: 500px; height: 456px;
    background: radial-gradient(ellipse at 32% 50%, #cfd6de 0%, #e7ebef 45%, #f7f8fa 75%, #ffffff 100%);
  }

  .bar { position: absolute; }
  .bar--red-top { left: 925px; top: 0; width: 87px; height: 180px; background: var(--red); }
  .bar--navy-mid { left: 805px; top: 144px; width: 55px; height: 173px; background: var(--navy); }
  .bar--red-mid { left: 641px; top: 281px; width: 95px; height: 36px; background: var(--red-dark); }

  .contact { position: absolute; left: 520px; top: 30px; width: 222px; text-align: right; }
  .contact__title { font-size: 22px; font-weight: 600; color: var(--red); letter-spacing: 0.5px; text-align: left; margin-left: 53px; }
  .contact__line { display: flex; justify-content: flex-end; align-items: center; gap: 8px; font-size: 16px; font-weight: 500; color: var(--ink); margin-top: 6px; }
  .contact__line:first-of-type { margin-top: 10px; }
  .contact__icon { width: 13px; height: 13px; fill: var(--ink); }

  .service { position: absolute; display: flex; align-items: center; color: var(--white); }
  .service--memory { left: 805px; top: 44px; width: 395px; height: 100px; background: var(--navy); padding-left: 18px; }
  .service--cheat { left: 641px; top: 180px; width: 414px; height: 101px; background: var(--red); padding-left: 18px; }
  .service--intel { left: 481px; top: 317px; width: 422px; height: 102px; background: var(--navy); padding-left: 18px; }
  .service__icon { width: 52px; height: 52px; flex: none; margin-right: 18px; }
  .service__title { font-size: 23px; font-weight: 600; letter-spacing: 0.5px; line-height: 1.1; }
  .service__text { font-size: 15.5px; font-weight: 500; line-height: 1.25; margin-top: 4px; }

  .cta { position: absolute; left: 922px; top: 291px; width: 240px; }
  .cta__title { font-size: 23px; font-weight: 600; color: var(--red); letter-spacing: 0.5px; white-space: nowrap; }
  .cta__text { font-size: 15.5px; font-weight: 500; color: var(--grey-text); line-height: 1.3; margin-top: 8px; }

  .cta-guide { position: absolute; left: 0; top: 0; }
</style>
</head>
<body>
<main class="cover">

  <svg class="backdrop" width="1200" height="456" viewBox="0 0 1200 456" aria-hidden="true">
    <polygon points="455,0 1200,0 1200,456 455,456 520,300 455,160" fill="var(--mist-light)"/>
    <polygon points="745,0 1200,0 1200,180 1055,180 1055,281 905,281 905,456 745,456" fill="var(--mist)"/>
    <polygon points="480,150 800,150 800,300 480,300" fill="var(--white)" opacity="0.6"/>
  </svg>

  <div class="hero-visual" role="img" aria-label="Illustration of a white humanoid robot head with glowing blue eyes in front of a faint grey network of connected dots"></div>

  <div class="bar bar--red-top"></div>
  <div class="bar bar--navy-mid"></div>
  <div class="bar bar--red-mid"></div>

  <section class="contact">
    <h2 class="contact__title">CONTACT INFO</h2>
    <p class="contact__line">+34 900 318 274
      <svg class="contact__icon" viewBox="0 0 24 24"><path d="M6.6 10.8c1.4 2.8 3.8 5.1 6.6 6.6l2.2-2.2c.3-.3.7-.4 1-.2 1.1.4 2.300.6 3.6.6.6 0 1 .4 1 1V20c0 .6-.4 1-1 1C10.6 21 3 13.4 3 4c0-.6.4-1 1-1h3.5c.6 0 1 .4 1 1 0 1.3.2 2.5.6 3.6.1.3 0 .7-.2 1L6.6 10.8z"/></svg>
    </p>
    <p class="contact__line">info@quillmora.com
      <svg class="contact__icon" viewBox="0 0 24 24"><path d="M2 5h20v14H2z" fill="var(--ink)"/><path d="M3 6l9 7 9-7" fill="none" stroke="var(--white)" stroke-width="1.6"/></svg>
    </p>
  </section>

  <article class="service service--memory">
    <svg class="service__icon" viewBox="0 0 52 52" fill="none" stroke="#fff" stroke-width="2.4" stroke-linejoin="round">
      <rect x="2" y="2" width="48" height="48" rx="8" stroke-width="1.6"/>
      <path d="M26 10l13 5v10c0 8-6 14-13 17-7-3-13-9-13-17V15z"/>
      <path d="M20 26l5 5 8-9"/>
    </svg>
    <div>
      <h3 class="service__title">MEMORY GUARD</h3>
      <p class="service__text">Virtualization-based toolkit for<br>dynamic code and data interception</p>
    </div>
  </article>

  <article class="service service--cheat">
    <svg class="service__icon" viewBox="0 0 52 52" fill="none" stroke="#fff" stroke-width="2.4" stroke-linejoin="round">
      <path d="M26 6l17 6v13c0 10-8 18-17 21-9-3-17-11-17-21V12z"/>
      <path d="M18 22h16M20 28h12"/>
    </svg>
    <div>
      <h3 class="service__title">ANTI-CHEAT</h3>
      <p class="service__text">Smash advanced cheaters leveraging<br>deep learning technologies</p>
    </div>
  </article>

  <article class="service service--intel">
    <svg class="service__icon" viewBox="0 0 52 52" fill="#fff" stroke="#fff" stroke-width="2">
      <circle cx="26" cy="26" r="7"/>
      <path d="M26 19V8M26 33v11M19 26H8M33 26h11M21 21l-7-7M31 31l7 7M31 21l7-7M21 31l-7 7"/>
      <circle cx="26" cy="7" r="3"/><circle cx="26" cy="45" r="3"/><circle cx="7" cy="26" r="3"/><circle cx="45" cy="26" r="3"/>
      <circle cx="13" cy="13" r="3"/><circle cx="39" cy="39" r="3"/><circle cx="39" cy="13" r="3"/><circle cx="13" cy="39" r="3"/>
    </svg>
    <div>
      <h3 class="service__title">THREAT INTELLIGENCE</h3>
      <p class="service__text">Seasoned cybersecurity experts to<br>analyze relevant threat intelligence</p>
    </div>
  </article>

  <svg class="cta-guide" width="1200" height="456" viewBox="0 0 1200 456" aria-hidden="true">
    <polyline points="1148,306 1186,306 1186,412 1106,412 1106,426" fill="none" stroke="var(--guide)" stroke-width="1.5"/>
    <polygon points="1092,427 1120,427 1106,443" fill="var(--red)"/>
  </svg>

  <section class="cta">
    <h2 class="cta__title">WORK WITH US ?</h2>
    <p class="cta__text">Build your solution over the<br>solid foundation provided<br>by our top class development<br>kit.</p>
  </section>

</main>
</body>
</html>
```